Letterhead to coordinate with business card

I am needing a docx template and print file for a letterhead to co-ordinate with my newly designed logo and business card.

```html
<!DOCTYPE html>
<html lang="en">
<head>
<meta charset="utf-8">
<title>Harbour Plan Services – Letterhead</title>
<link rel="stylesheet" href="https://fonts.googleapis.com/css2?family=Arimo:wght@400;700&family=Questrial&display=swap">
<style>
  :root {
    --backdrop: #acabac;
    --paper: #ffffff;
    --teal: #007f80;
    --magenta: #aa3167;
    --ink: #4d4d4f;
    --band-text: #ffffff;
  }
  * { box-sizing: border-box; margin: 0; padding: 0; }
  html, body { width: 1200px; height: 934px; overflow: hidden; }
  body { background: var(--backdrop); position: relative; font-family: "Arimo", Arial, sans-serif; }

  .letterhead {
    position: absolute; left: 322px; top: 74px;
    width: 556px; height: 785px;
    background: var(--paper);
  }
  .header-band {
    position: absolute; left: 0; top: 31px;
    width: 100%; height: 47px;
    background: var(--teal);
  }
  .header-band .accent-block {
    position: absolute; left: 0; top: 0;
    width: 77px; height: 100%;
    background: var(--magenta);
  }
  .contact-list {
    position: absolute; left: 238px; top: 7px;
    list-style: none; color: var(--band-text);
    font-size: 9.4px; line-height: 11.4px;
  }
  .contact-list li { display: flex; align-items: center; gap: 4px; }
  .contact-list svg { width: 8px; height: 8px; flex: none; }
  .band-divider {
    position: absolute; left: 411px; top: 10px;
    width: 1px; height: 30px; background: var(--band-text);
  }
  .postal-address {
    position: absolute; left: 420px; top: 18px;
    font-style: normal; color: var(--band-text);
    font-size: 9.4px; line-height: 11.4px;
  }
  .brand-name {
    position: absolute; left: 45px; top: 86px;
    font-family: "Questrial", "Century Gothic", sans-serif;
    font-size: 14px; color: var(--magenta); letter-spacing: 0.3px;
  }

  .letter-body { position: absolute; left: 50px; top: 240px; width: 458px; color: var(--ink); }
  .salutation {
    font-family: "Questrial", "Century Gothic", sans-serif;
    font-weight: 700; font-size: 13.4px; margin-bottom: 20px;
    -webkit-text-stroke: 0.3px var(--ink);
  }
  .letter-body p.copy { font-size: 9.5px; line-height: 11.4px; margin-bottom: 10.5px; }
  .closing {
    font-family: "Questrial", "Century Gothic", sans-serif;
    font-size: 7.6px; font-weight: 700; margin-top: 21px;
    -webkit-text-stroke: 0.2px var(--ink);
  }
  .signature {
    margin-top: 24px; width: 92px; height: 27px;
    background: linear-gradient(90deg, #e4e4e5, #d6d6d8);
    border-radius: 2px;
  }
</style>
</head>
<body>
  <main class="letterhead">
    <header class="header-band">
      <div class="accent-block"></div>
      <ul class="contact-list">
        <li>
          <svg viewBox="0 0 10 10" aria-hidden="true"><circle cx="5" cy="5" r="5" fill="#fff"/><path d="M3.2 2.6c.3-.3.6-.2.8.1l.4.7c.1.2 0 .4-.2.6l-.2.2c.3.6.8 1.1 1.4 1.4l.2-.2c.2-.2.4-.3.6-.2l.7.4c.3.2.4.5.1.8l-.4.4C5.6 7 2.9 4.3 2.8 3z" fill="#007f80"/></svg>
          0400 123 456
        </li>
        <li>
          <svg viewBox="0 0 10 10" aria-hidden="true"><circle cx="5" cy="5" r="5" fill="#fff"/><rect x="2.5" y="3.3" width="5" height="3.4" fill="none" stroke="#007f80" stroke-width=".8"/><path d="M2.5 3.4 5 5.3l2.5-1.9" fill="none" stroke="#007f80" stroke-width=".8"/></svg>
          hello@harbourplanservices.com.au
        </li>
        <li>
          <svg viewBox="0 0 10 10" aria-hidden="true"><circle cx="5" cy="5" r="5" fill="#fff"/><circle cx="5" cy="5" r="2.8" fill="none" stroke="#007f80" stroke-width=".7"/><ellipse cx="5" cy="5" rx="1.2" ry="2.8" fill="none" stroke="#007f80" stroke-width=".6"/><path d="M2.2 5h5.6" stroke="#007f80" stroke-width=".6"/></svg>
          www.harbourplanservices.com.au
        </li>
      </ul>
      <div class="band-divider"></div>
      <address class="postal-address">PO Box 42<br>Lakeview NSW 2999</address>
    </header>

    <div class="brand-name">Harbour Plan Services</div>

    <section class="letter-body">
      <p class="salutation">Dear Mr. Hale,</p>
      <p class="copy">Lorem ipsum dolor sit amet, consectetuer adipiscing elit, sed diam nonmmy nibh euismod tincidunt ut laor eet dolore magna aliquam erat volutpat. Ut wisi enim ad minim veniam, quis nostrud exerci tationmcorper suscipit lobortis nisl ut aliquip ex ea commodo consequat. Duis autem vel eum iriure dolor in hendrerit in vulputate velit esse molestie consequat, vel illum dolore eu feugiat</p>
      <p class="copy">Rorem ipsum dolor sit amet, consectetuer adipiscing elit, sed diam nonmmy nibh euismod tincidunt ut laor eet dolore magna aliquam erat volutpat. Ut wisi enim ad minim veniam, quis nostrud exerci tationmcorper suscipit lobortis nisl ut aliquip ex ea commodo consequat. Duis autem vel eum iriure dolor in hendrerit in vulputate velit esse molest</p>
      <p class="copy">Dorem ipsum dolor sit amet, consectetuer adipiscing elit, sed diam nonmmy nibh euismod tincidunt ut laor eet dolore magna aliquam erat volutpat. Ut wisi enim ad minim veniam, quis nostrud exerci tationmcorper suscipit lobortis nisl ut aliquip ex ea commodo consequat. Duis autem vel eum iriure dolor in hendrerit in suscipit lobortis nisl ut aliquip ex ea commodo consequat. Duis autem vel eum iriure dolor in hendrerit in vulputate velit esse molestie consequat, vel illum</p>
      <p class="copy">Sorem ipsum dolor sit amet, consectetuer adipiscing elit, sed diam nonmmy nibh euismod tincidunt ut laor eet dolore magna aliquam erat volutpat. Ut wisi enim ad minim veniam, quis nostrud exerci tationmcorper suscipit lobortis nisl ut aliquip ex ea commodo consequat. Duis autem vel eum iriure dolor in</p>
      <p class="closing">Sincerely,</p>
      <div class="signature" role="img" aria-label="Handwritten signature of the sender"></div>
    </section>
  </main>
</body>
</html>
```